Social Media Application Design - Android and IOS

I am ready to go live with new social media app however I am not comfortable with the current design. It is a not interactive or attractive enough. Please note the splash screen is a green, so preference would be to keep a green theme although I am more than happy to consider other colours that would improve the design.
The attachment has the app screens that need to be redesigned. They may not need massive changes , however keen to go live so looking for inspired designers to support with this project and many others that I have, including ongoing work on this app.
Target Market(s)
Millenials
Industry/Entity Type
Social
Colors
Designer to choose colors to be used in the design.
Requirements
Must have
- Please see attached document for screens that I would like redesigned. It needs to work with Android and IOS. I am looking for the design and not the functionality.
Nice to have
- Highly interactive design. Please see polling functionality of Loomrix.
Should not have
- should not be complicated - simplicity is the key

```html
<!DOCTYPE html>
<html lang="en">
<head>
<meta charset="utf-8">
<title>Askly – App Screens</title>
<link href="https://fonts.googleapis.com/css2?family=Montserrat:wght@300;400;600;700&display=swap" rel="stylesheet">
<style>
:root{
  --bg:#e4e7ea;
  --screen:#ffffff;
  --green:#1fc98a;
  --green-dark:#16b57a;
  --lime:#cdee5c;
  --ink:#2a2f33;
  --muted:#a9b0b5;
  --line:#e3e7ea;
  --orange:#ff5a2c;
  --photo-a:#3a3a3a;
  --photo-b:#cfcac4;
}
*{box-sizing:border-box;margin:0;padding:0}
html,body{width:1200px;height:787px;overflow:hidden;background:var(--bg);font-family:"Montserrat",sans-serif;color:var(--ink)}
.board{display:grid;grid-template-columns:repeat(4,260px);grid-template-rows:repeat(2,372px);gap:14px 32px;padding:14px 32px}
.screen{position:relative;background:var(--screen);border-radius:16px;overflow:hidden;box-shadow:0 10px 24px rgba(40,60,70,.12)}
.appbar{height:54px;background:linear-gradient(100deg,var(--green) 30%,var(--lime));display:flex;align-items:center;padding:0 14px;color:#fff;font-size:11px;font-weight:600;gap:10px}
.appbar .title{flex:1;text-align:center;letter-spacing:.5px}
.appbar svg{flex:none}
.body{padding:14px 18px}
.h-light{font-weight:300;font-size:21px;line-height:1.05;color:#8d969c}
.h-bold{font-weight:700;font-size:21px;line-height:1.05}
.chips{display:flex;flex-wrap:wrap;gap:6px;margin:10px 0}
.chip{font-size:9px;font-weight:600;padding:5px 11px;border-radius:12px;background:var(--green);color:#fff}
.chip.ghost{background:#fff;color:var(--green);border:1.5px solid var(--green)}
.rule{height:1px;background:var(--line);margin:8px 0 12px}
.btn{position:absolute;left:18px;right:18px;bottom:16px;height:34px;border-radius:17px;background:linear-gradient(90deg,var(--green),#3ad99c);color:#fff;font-size:11px;font-weight:600;display:flex;align-items:center;justify-content:center}
.btn .go{position:absolute;right:8px;width:18px;height:18px;border-radius:50%;background:#fff;display:flex;align-items:center;justify-content:center}
.label{font-size:8px;color:var(--muted)}
.slots{display:flex;gap:10px;justify-content:flex-end;margin-top:-6px}
.slot{width:46px;height:46px;border:1.5px dashed #cdd3d7;border-radius:8px;display:flex;flex-direction:column;align-items:center;justify-content:center;gap:3px;font-size:6px;color:var(--muted)}
/* feed */
.search{margin:10px 14px 6px;height:24px;border-radius:12px;background:#f3f5f6;font-size:8px;color:var(--muted);display:flex;align-items:center;padding:0 10px;gap:6px}
.post{margin:8px 14px;padding:8px;border-radius:8px;box-shadow:0 3px 10px rgba(0,0,0,.07);position:relative}
.post .meta{display:flex;align-items:center;gap:6px}
.avatar{width:22px;height:22px;border-radius:50%;background:linear-gradient(135deg,#b9a18d,#6e6257)}
.name{font-size:8px;font-weight:600}
.time{font-size:6px;color:var(--muted)}
.q{font-size:8px;font-weight:600;margin:5px 0}
.photo{height:72px;border-radius:4px;background:linear-gradient(120deg,var(--photo-a) 45%,var(--photo-b))}
.acts{position:absolute;top:8px;right:10px;display:flex;gap:6px}
.votes{position:absolute;right:-4px;top:40px;width:32px;height:32px;background:var(--green);color:#fff;font-size:9px;font-weight:700;text-align:center;line-height:1;padding-top:7px;border-radius:3px}
.votes small{display:block;font-size:6px;font-weight:400}
.fab{position:absolute;right:16px;bottom:16px;width:30px;height:30px;border-radius:50%;background:var(--orange);display:flex;align-items:center;justify-content:center;box-shadow:0 4px 10px rgba(255,90,44,.4)}
/* profile */
.profile-head{height:150px;background:linear-gradient(110deg,var(--green) 40%,var(--lime));color:#fff;text-align:center;padding-top:14px;position:relative}
.profile-head .back{position:absolute;left:14px;top:16px}
.portrait{width:58px;height:58px;border-radius:50%;margin:6px auto 8px;background:linear-gradient(135deg,#5dc3e8,#d96a5a);border:3px solid rgba(255,255,255,.5)}
.pname{font-size:12px;font-weight:700}
.pmail{font-size:8px;opacity:.9}
.menu{padding:16px 22px}
.menu li{list-style:none;margin-bottom:11px;position:relative}
.menu b{display:block;font-size:10px;font-weight:600}
.menu span{font-size:6.5px;color:var(--muted)}
.toggle{position:absolute;right:0;top:2px;width:30px;height:14px;border-radius:7px;background:var(--green);font-size:6px;color:#fff;padding:3px 5px}
/* filter */
.panel{position:absolute;left:10px;right:10px;top:64px;bottom:14px;background:var(--green);border-radius:14px;padding:14px;color:#fff}
.panel h4{font-size:9px;font-weight:600;margin:8px 0 5px}
.panel .chip{background:rgba(255,255,255,.22);font-size:8px}
.panel .chip.on{background:#fff;color:var(--green)}
.slider{height:3px;background:rgba(255,255,255,.4);border-radius:2px;position:relative;margin:14px 0 6px}
.slider i{position:absolute;left:12%;top:-5px;width:13px;height:13px;border-radius:50%;background:#fff}
.km{font-size:7px;text-align:right}
.ok{position:absolute;right:14px;top:132px;width:30px;height:30px;border-radius:50%;background:var(--orange);display:flex;align-items:center;justify-content:center}
/* audio */
.rec{display:flex;gap:10px;justify-content:flex-end;margin-top:-4px}
.rec .slot{font-size:6px;text-align:center}
</style>
</head>
<body>
<main class="board">

<!-- Post a question: image options -->
<section class="screen">
  <header class="appbar"><svg width="14" height="10" viewBox="0 0 14 10"><path d="M13 5H1M5 1 1 5l4 4" stroke="#fff" stroke-width="1.6" fill="none"/></svg><span class="title">Post a Question</span><span style="width:14px"></span></header>
  <div class="body">
    <p class="h-light">Your Question</p><p class="h-bold">Is about</p>
    <div class="chips"><span class="chip">Science</span><span class="chip">Health</span><span class="chip">Religion</span></div>
    <div class="rule"></div>
    <p class="h-light">What is your</p><p class="h-bold">Question?</p>
    <div class="rule"></div>
    <p class="h-light">What are the</p><p class="h-bold">Options?</p>
    <div class="slots">
      <div class="slot"><svg width="14" height="11" viewBox="0 0 14 11"><rect x="1" y="2" width="12" height="8" rx="1.5" stroke="#b8c0c5" fill="none"/><circle cx="7" cy="6" r="2" stroke="#b8c0c5" fill="none"/></svg></div>
      <div class="slot"><svg width="12" height="12" viewBox="0 0 12 12"><path d="M6 1v10M1 6h10" stroke="#b8c0c5" stroke-width="1.4"/></svg></div>
    </div>
    <p class="label">Images</p>
  </div>
  <div class="btn">Post<span class="go"><svg width="8" height="8" viewBox="0 0 8 8"><path d="M1 4h6M4 1l3 3-3 3" stroke="#1fc98a" stroke-width="1.3" fill="none"/></svg></span></div>
</section>

<!-- Feed -->
<section class="screen">
  <header class="appbar"><svg width="14" height="10" viewBox="0 0 14 10"><path d="M1 2h12M1 5h9M1 8h12" stroke="#fff" stroke-width="1.6"/></svg><span class="title">Askly</span><svg width="14" height="10" viewBox="0 0 14 10"><path d="M1 3h12M1 7h12" stroke="#fff" stroke-width="1.4"/><circle cx="9" cy="3" r="1.6" fill="#fff"/><circle cx="5" cy="7" r="1.6" fill="#fff"/></svg></header>
  <div class="search"><svg width="8" height="8" viewBox="0 0 8 8"><circle cx="3.4" cy="3.4" r="2.6" stroke="#a9b0b5" fill="none"/><path d="M5.5 5.5 7.5 7.5" stroke="#a9b0b5"/></svg>Search something</div>
  <article class="post"><div class="meta"><span class="avatar"></span><div><p class="name">Marisol Ventra</p><p class="time">1h ago</p></div></div><p class="q">Who is your favorite music artist?</p><div class="photo" role="img" aria-label="Black and white photo of a musician performing"></div><span class="votes">15<small>Votes</small></span></article>
  <article class="post"><div class="meta"><span class="avatar"></span><div><p class="name">Marisol Ventra</p><p class="time">3h ago</p></div></div><p class="q">Who is your favorite music artist?</p><div class="photo" role="img" aria-label="Black and white photo of a singer on stage"></div><span class="votes">18<small>Votes</small></span></article>
  <span class="fab"><svg width="12" height="12" viewBox="0 0 12 12"><path d="M6 1v10M1 6h10" stroke="#fff" stroke-width="2"/></svg></span>
</section>

<!-- Profile menu -->
<section class="screen">
  <header class="profile-head">
    <svg class="back" width="14" height="10" viewBox="0 0 14 10"><path d="M13 5H1M5 1 1 5l4 4" stroke="#fff" stroke-width="1.6" fill="none"/></svg>
    <div class="portrait" role="img" aria-label="Profile photo of the user"></div>
    <p class="pname">Theo Brannick</p><p class="pmail">theo.brannick@mailbox.com</p>
  </header>
  <ul class="menu">
    <li><b>Home</b><span>All categories items</span></li>
    <li><b>My profile</b><span>Change your personal settings</span></li>
    <li><b>My activities</b><span>See all your activities</span></li>
    <li><b style="color:var(--green)">• Notification</b><span>Settings for notifications</span><span class="toggle">ON</span></li>
    <li><b>Contact us</b><span>Send us your feedback</span></li>
    <li><b>Logout</b></li>
  </ul>
</section>

<!-- Post a question: text options -->
<section class="screen">
  <header class="appbar"><svg width="14" height="10" viewBox="0 0 14 10"><path d="M13 5H1M5 1 1 5l4 4" stroke="#fff" stroke-width="1.6" fill="none"/></svg><span class="title">Post a Question</span><span style="width:14px"></span></header>
  <div class="body">
    <p class="h-light">Your Question</p><p class="h-bold">Is about</p>
    <div class="chips"><span class="chip">Science</span><span class="chip">Health</span><span class="chip">Religion</span></div>
    <div class="rule"></div>
    <p class="h-light">What is your</p><p class="h-bold">Question?</p>
    <div class="rule"></div>
    <p class="h-light">What are the</p><p class="h-bold">Options?</p>
    <p class="label" style="text-align:right;color:var(--green);font-size:10px">≡+</p>
    <div class="rule"></div>
  </div>
  <div class="btn">Post<span class="go"><svg width="8" height="8" viewBox="0 0 8 8"><path d="M1 4h6M4 1l3 3-3 3" stroke="#1fc98a" stroke-width="1.3" fill="none"/></svg></span></div>
</section>

<!-- Filter -->
<section class="screen">
  <header class="appbar"><svg width="14" height="10" viewBox="0 0 14 10"><path d="M1 2h12M1 5h9M1 8h12" stroke="#fff" stroke-width="1.6"/></svg><span class="title">Askly</span><svg width="14" height="10" viewBox="0 0 14 10"><path d="M1 3h12M1 7h12" stroke="#fff" stroke-width="1.4"/><circle cx="9" cy="3" r="1.6" fill="#fff"/><circle cx="5" cy="7" r="1.6" fill="#fff"/></svg></header>
  <div class="panel">
    <h4>Interests</h4>
    <div class="chips" style="margin:0"><span class="chip on">Animals</span><span class="chip">Humans</span><span class="chip">Education</span><span class="chip">Public</span></div>
    <h4>Questions</h4>
    <div class="chips" style="margin:0"><span class="chip on">All Questions</span><span class="chip">My Questions</span></div>
    <h4>Search radius</h4>
    <div class="slider"><i></i></div><p class="km">50 km</p>
    <h4>Sort by</h4>
    <div class="chips" style="margin:0"><span class="chip on">Newest</span><span class="chip">Popular</span><span class="chip">Trending</span></div>
  </div>
  <span class="ok"><svg width="12" height="10" viewBox="0 0 12 10"><path d="M1 5l3.5 3.5L11 1" stroke="#fff" stroke-width="2" fill="none"/></svg></span>
</section>

<!-- Feed -->
<section class="screen">
  <header class="appbar"><svg width="14" height="10" viewBox="0 0 14 10"><path d="M1 2h12M1 5h9M1 8h12" stroke="#fff" stroke-width="1.6"/></svg><span class="title">Askly</span><svg width="14" height="10" viewBox="0 0 14 10"><path d="M1 3h12M1 7h12" stroke="#fff" stroke-width="1.4"/><circle cx="9" cy="3" r="1.6" fill="#fff"/><circle cx="5" cy="7" r="1.6" fill="#fff"/></svg></header>
  <div class="search"><svg width="8" height="8" viewBox="0 0 8 8"><circle cx="3.4" cy="3.4" r="2.6" stroke="#a9b0b5" fill="none"/><path d="M5.5 5.5 7.5 7.5" stroke="#a9b0b5"/></svg>Search something</div>
  <article class="post"><div class="meta"><span class="avatar"></span><div><p class="name">Marisol Ventra</p><p class="time">1h ago</p></div></div><p class="q">Who is your favorite music artist?</p><div class="photo" role="img" aria-label="Black and white photo of a musician performing"></div><span class="votes">15<small>Votes</small></span></article>
  <article class="post"><div class="meta"><span class="avatar"></span><div><p class="name">Marisol Ventra</p><p class="time">3h ago</p></div></div><p class="q">Who is your favorite music artist?</p><div class="photo" role="img" aria-label="Black and white photo of a singer on stage"></div><span class="votes">18<small>Votes</small></span></article>
  <span class="fab"><svg width="12" height="12" viewBox="0 0 12 12"><path d="M6 1v10M1 6h10" stroke="#fff" stroke-width="2"/></svg></span>
</section>

<!-- Topic selection -->
<section class="screen">
  <header class="appbar"><svg width="14" height="10" viewBox="0 0 14 10"><path d="M13 5H1M5 1 1 5l4 4" stroke="#fff" stroke-width="1.6" fill="none"/></svg><span class="title">Post a Question</span><span style="width:14px"></span></header>
  <div class="search"><svg width="8" height="8" viewBox="0 0 8 8"><circle cx="3.4" cy="3.4" r="2.6" stroke="#a9b0b5" fill="none"/><path d="M5.5 5.5 7.5 7.5" stroke="#a9b0b5"/></svg>Search topic</div>
  <div class="body">
    <p class="h-light">What is your</p><p class="h-bold">Question about</p>
    <div class="chips">
      <span class="chip">Science</span><span class="chip ghost">Technology</span><span class="chip ghost">Gadgets</span>
      <span class="chip">Health</span><span class="chip ghost">Fashion</span><span class="chip ghost">Beauty</span>
      <span class="chip ghost">Travel</span><span class="chip">Religion</span><span class="chip ghost">History</span>
      <span class="chip ghost">Language</span><span class="chip ghost">Education</span><span class="chip ghost">Business</span>
      <span class="chip ghost">Finance</span><span class="chip">My Country</span><span class="chip ghost">My Cities</span>
    </div>
  </div>
  <div class="btn">Continue<span class="go"><svg width="8" height="8" viewBox="0 0 8 8"><path d="M1 4h6M4 1l3 3-3 3" stroke="#1fc98a" stroke-width="1.3" fill="none"/></svg></span></div>
</section>

<!-- Post a question: audio options -->
<section class="screen">
  <header class="appbar"><svg width="14" height="10" viewBox="0 0 14 10"><path d="M13 5H1M5 1 1 5l4 4" stroke="#fff" stroke-width="1.6" fill="none"/></svg><span class="title">Post a Question</span><span style="width:14px"></span></header>
  <div class="body">
    <p class="h-light">Your Question</p><p class="h-bold">Is about</p>
    <div class="chips"><span class="chip">Science</span><span class="chip">Health</span><span class="chip">Religion</span></div>
    <div class="rule"></div>
    <p class="h-light">What is your</p><p class="h-bold">Question?</p>
    <div class="rule"></div>
    <p class="h-light">What are the</p><p class="h-bold">Options?</p>
    <div class="rec">
      <div class="slot"><svg width="10" height="13" viewBox="0 0 10 13"><rect x="3" y="1" width="4" height="7" rx="2" fill="#1fc98a"/><path d="M1 6a4 4 0 0 0 8 0M5 10v2" stroke="#1fc98a" fill="none"/></svg>1:30<br>Record Option 1</div>
      <div class="slot"><svg width="10" height="13" viewBox="0 0 10 13"><rect x="3" y="1" width="4" height="7" rx="2" fill="#b8c0c5"/><path d="M1 6a4 4 0 0 0 8 0M5 10v2" stroke="#b8c0c5" fill="none"/></svg>Record Option 2</div>
    </div>
    <p class="label">Audio</p>
  </div>
  <div class="btn">Post<span class="go"><svg width="8" height="8" viewBox="0 0 8 8"><path d="M1 4h6M4 1l3 3-3 3" stroke="#1fc98a" stroke-width="1.3" fill="none"/></svg></span></div>
</section>

</main>
</body>
</html>
```